WordPress design for BraxtonVell.com

*****
OVERVIEW
*****
BraxtonVell.com needs a fresh, clean, professional design that effectively illustrates its talent in a thoughtful, impressive, and impactful way.
Vell Architecture & Interiors (www.braxtonvell.com) is a well-established, prestigious, well-publicized New England USA architecture firm. Founded in 1996, the privately-held company specializes in high-end residential projects with a focus on classic New England style architecture.
Business contact information is as noted below:
Address:
Vell Architecture & Interiors
87 Orchard Terrace
Needham, MA 02817
Telephone:
617-555-0138
781-555-0274
Email:
info@braxtonvell.com
An excerpt from the current site describes the outfit with this:
"Our architecture and interior design practices are centered around the philosophy that successful living spaces combine a focus on richly articulated detail and an in-depth knowledge of quality construction techniques."
*****
DESIGN RESEARCH
*****
In reviewing design ideas, the following sites were appealing:
Good
- Marcus Thorne Architects (http://mtaarchitects-example.com/) - Simple and clean, but almost too simple.
Better
- Penrose Galt Architecture (http://www.penrosegalt-example.com/) - Direct portfolio access. Simple and clean.
Best
- Brimwell Architects (http://www.brimwellarchitects-example.com/) - Clean, simple, easy to navigate
- QRV Architecture & Interiors (http://www.qrv-architects-example.com/) - Excellent use of high-resolution media, transitions, and navigation.
Here is an example of what is NOT desired:
Tolland Pryce Architects (http://www.tollandpryce-example.com/) - Cluttered, tight landing page. Uncertain navigation.
*****
OTHER DETAILS
*****
The grey in the Vell Architecture & Interiors logo is hex 636363. The font is unknown.
Updates
Project Deadline Extended
Reason: Hello everyone,
Thank you for your continued patience with this project. As it turns out, a critical member of the decision making team on our client's end has been out of the office this week. She will be back next week and is ready to be fully engaged with this. That said, we are extending the contest for at least 5 days. Next week will be much more active.
Thank you for your understanding.
Glasswick Technology Services
Project Deadline Extended
Reason: Hello everyone,
The customer was on vacation and only returned Monday of this week. That said, we need to extend the deadline for 5 days to afford time for review and comment.
Thank you for your patience! The designs submitted thus far are fantastic!
Thanks again,
Project Deadline Extended
Reason: Hello,
With so many designs, the customer is taking longer than anticipated to review them. They are looking at them offline and will process a large batch of comments when ready.
That said, the contest is being extended again.
Thank you for your continued patience.
Project Deadline Extended
Reason: Hello,
Because there are 108 designs to review and comment on, this is taking much longer than anticipated. That said, the contest is being extended another 5 days to ensure the customer has the desired outcome.
Thank you,
Target Market(s)
- Would-be clients
- Landowners
- Construction firms and general contractors
- High-end residential component manufacturers
- Media outlets
- All others interested in high-end residential architecture and interior design
Industry/Entity Type
Architecture
Requirements
Must have
- - Lots of media capabilities, such as embedded video (via ClipStream is fine), project image gallery, sliders for various functions, and social media integrations
- - At least one large slider on the landing page is critical, as well as space for standard lead-in things, such as news/events, opportunities, project highlights, and the likes
- - A high-resolution project showcase - finished projects and works in progress - is critical
- - A place to highlight business partners with the potential for reciprocation
- Form capabilities for things like information requests and general contacts from the public
- - Design must be handed off in a logically-layered (for WordPress) PSD with any and all additional source files provided (e.g. Photoshop, Illustrator, fonts, etc)
Nice to have
- - The WordPress design should be capable of fitting into the very popular FernLayouts Trellis theme.

```html
<!DOCTYPE html>
<html lang="en">
<head>
<meta charset="utf-8">
<title>Vell Architecture &amp; Interiors</title>
<link rel="stylesheet" href="https://fonts.googleapis.com/css2?family=Open+Sans:wght@400;600;700&display=swap">
<style>
:root{
  --ink:#111111;
  --panel:#141414;
  --grey:#636363;
  --body:#bdbdbd;
  --white:#ffffff;
  --accent:#e3b04b;
}
*{margin:0;padding:0;box-sizing:border-box}
html,body{width:764px;height:1200px;overflow:hidden;background:var(--white)}
body{position:relative;font-family:"Open Sans",Arial,sans-serif;color:var(--ink)}
.site-header{position:absolute;left:56px;top:0;width:652px;height:72px}
.main-nav{position:absolute;left:0;top:30px;display:flex;gap:13px;font-size:8px;color:var(--grey)}
.brand{display:flex;align-items:center;gap:6px;color:var(--grey);font-size:10px;font-weight:600;white-space:nowrap}
.brand-mark{width:9px;height:9px;background:var(--grey);display:block}
.site-header .brand{position:absolute;right:0;top:28px}
.photo{position:absolute}
.panel{position:absolute;background:var(--panel);color:var(--white);padding:14px 14px}
.panel h2{font-size:10px;font-weight:700;letter-spacing:.5px;text-transform:uppercase;margin-bottom:8px}
.panel p{font-size:7.5px;line-height:1.55;color:var(--body)}
.panel .more{display:block;font-size:7px;color:var(--white);margin-top:6px;text-decoration:underline}
.panel .loc{position:absolute;bottom:12px;left:14px;right:14px;font-size:7px;color:var(--white);line-height:1.5}
.panel .loc b{display:block;font-weight:700}
.panel .link{color:var(--accent);font-size:7px;display:block;margin-top:8px}
.site-footer{position:absolute;left:56px;top:1048px;width:652px;height:140px}
.site-footer h3{font-size:9px;font-weight:700;text-transform:uppercase;margin-bottom:8px}
.contact{position:absolute;left:0;top:0;width:170px}
.contact-cols{display:flex;gap:10px;font-size:6.5px;line-height:1.7;color:var(--grey)}
.contact-cols .addr{width:66px}
.contact-cols .hl{color:var(--accent)}
.pubs{position:absolute;left:190px;top:0;width:300px}
.pubs-cols{display:flex;gap:60px}
.pubs ul{list-style:none;font-size:6.5px;line-height:1.7;color:var(--grey)}
.footer-brand{position:absolute;right:0;top:4px;display:flex;flex-direction:column;align-items:center}
.social{display:flex;gap:6px;justify-content:center;margin-top:12px}
.social span{width:15px;height:15px;border-radius:50%;background:var(--ink);display:block}
.copyright{position:absolute;left:0;top:128px;font-size:6.5px;color:var(--grey)}
</style>
</head>
<body>
<header class="site-header">
  <nav class="main-nav">
    <span>Home</span><span>About</span><span>Architecture</span><span>Interior Design</span><span>Works in progress</span><span>Renovations And Additions</span><span>Recognition</span><span>Affiliates</span>
  </nav>
  <div class="brand"><span class="brand-mark"></span>Vell Architecture &amp; Interiors</div>
</header>

<div class="photo" role="img" aria-label="Large warm living room interior with stone fireplace and wood floors" style="left:56px;top:76px;width:434px;height:301px;background:linear-gradient(135deg,#5a4332,#b08a63 55%,#3a2a1f)"></div>
<div class="photo" role="img" aria-label="Modern house terrace lit at dusk with pool" style="left:490px;top:76px;width:218px;height:166px;background:linear-gradient(160deg,#2a3a36,#8a8e77 60%,#1d2622)"></div>
<section class="panel" style="left:490px;top:242px;width:218px;height:135px">
  <h2>About Us</h2>
  <p>Vell Architecture &amp; Interiors is a New England firm specializing in architecture and interior design for custom residences. Since its founding in 1996, our team has shaped homes rich with detail and built with quality construction.</p>
  <span class="more">More Info...</span>
</section>

<section class="panel" style="left:56px;top:377px;width:144px;height:171px">
  <h2>Architecture</h2>
  <p>Our architecture practice designs homes that combine a careful focus on detail with sound building knowledge.</p>
  <span class="more">More Info...</span>
  <div class="loc">Location:<b>CHATHAM - MONROE ISLAND #1</b></div>
</section>
<div class="photo" role="img" aria-label="Bright kitchen with island and pendant lights" style="left:200px;top:377px;width:233px;height:171px;background:linear-gradient(135deg,#e9e5de,#8f7a63 60%,#3c342c)"></div>
<div class="photo" role="img" aria-label="Living room with mustard armchairs and tall draped windows" style="left:433px;top:377px;width:275px;height:383px;background:linear-gradient(170deg,#6b6660,#c9bfae 50%,#8a6c3e)"></div>

<div class="photo" role="img" aria-label="Patterned red armchair beside a window" style="left:56px;top:548px;width:144px;height:212px;background:linear-gradient(150deg,#d9d6d0,#b2563e 60%,#5c4a3d)"></div>
<section class="panel" style="left:200px;top:548px;width:233px;height:212px">
  <h2>Renovations And<br>Additions</h2>
  <p>Our renovation and addition work extends existing homes with care for their original character and proportion.</p>
  <span class="more">More Info...</span>
  <div class="loc">Location:<b>CHATHAM - MONROE ISLAND #1</b></div>
</section>

<section class="panel" style="left:56px;top:760px;width:244px;height:120px">
  <h2>Affiliates</h2>
  <p>We value lasting relationships with builders, craftsmen and suppliers who share our standards. These trusted partners help bring each home to completion with precision and care.</p>
  <span class="more">More Info...</span>
</section>
<div class="photo" role="img" aria-label="Red patterned armchair in a sunlit corner" style="left:56px;top:880px;width:244px;height:152px;background:linear-gradient(140deg,#ece8e2,#b9553d 55%,#4d3e34)"></div>
<div class="photo" role="img" aria-label="Classic white New England house with porches on a green lawn" style="left:300px;top:760px;width:240px;height:272px;background:linear-gradient(180deg,#9fc2e0,#e8e4da 55%,#5d7a3a)"></div>
<section class="panel" style="left:540px;top:810px;width:168px;height:222px">
  <h2>Harbor House Journal</h2>
  <p>Our Monroe Island residence is featured in the current issue of Harbor House Journal, with a full tour of the home and interiors.</p>
  <span class="link">Click here to download article</span>
  <div class="loc">Location:<b>CHATHAM - MONROE ISLAND #1</b></div>
</section>

<footer class="site-footer">
  <div class="contact">
    <h3>Contact Us</h3>
    <div class="contact-cols">
      <div class="addr">ADDRESS:<br>87 Orchard Terrace<br>Needham, MA 02817</div>
      <div><span class="hl">T:</span> 617-555-0138<br><span class="hl">T:</span> 781-555-0274<br>Email: info@braxtonvell.com</div>
    </div>
  </div>
  <div class="pubs">
    <h3>Featured Publications</h3>
    <div class="pubs-cols">
      <ul><li>Harbor Living</li><li>Shoreline Home Digest</li><li>Cape Coast Review</li><li>Seaside Cottage Quarterly</li><li>Timber Home Annual</li><li>Hearth &amp; Garden</li><li>Colonial Style Today</li></ul>
      <ul><li>Interior Notes</li><li>Dune Road Journal</li><li>Coastal Estates</li><li>Northern Builder</li><li>Residential Form</li></ul>
    </div>
  </div>
  <div class="footer-brand">
    <div class="brand"><span class="brand-mark"></span>Vell Architecture &amp; Interiors</div>
    <div class="social"><span></span><span></span><span></span><span></span></div>
  </div>
  <div class="copyright">Copyright © 2015 braxtonvell.com</div>
</footer>
</body>
</html>
```